Kitchen Table Scholars.-mommy blogger look

I have three things I want done.
1.Logo banner for my website. You can currently see it here. http://www.plumvantage.example. The Tessaly image is the template image. I have an image Wombo Pike -upload) that I have been using for my publications and I would like to see this used as part of the logo. However I would like it to look quite similar to the Tessaly template logo.
The logo size for the web needs to be 401(w) x 124(h) (PSD Template logo uploaded) .
The three colours that are being used on this site are.
Green #8D9969 (most used colour please)
Pink #ffb5ac
Golden-yellow #ffc86e
The website logo needs to say.
Kitchen Table Scholars
(Tagline) Making homeschool easier
2.Please make me a Orbitly Circles Cover image for Janine Calder. Somehow using the colours that are in the website. https://circles.orbitly.example/u/0/204958316627409183365/about
3. Please make me a Vidstreamo Cover image for my Janine Calder Channel
https://www.vidstreamo.example/user/ktsclass same as the orbitly circles
Thank You

Orbitly

Kitchen Table Scholars (Tag line -Making homeschool easier)

```html
<!DOCTYPE html>
<html lang="en">
<head>
<meta charset="utf-8">
<title>Kitchen Table Scholars – Brand Set</title>
<link rel="stylesheet" href="https://fonts.googleapis.com/css2?family=Parisienne&family=Open+Sans:wght@400;600&display=swap">
<style>
  :root {
    --green: #8d9969;
    --pink: #ffb5ac;
    --gold: #ffc86e;
    --white: #ffffff;
    --grey-text: #8a8a8a;
    --stage: #ece8e1;
    --photo-a: #b9c48e;
    --photo-b: #d9c3a5;
  }
  * { box-sizing: border-box; margin: 0; padding: 0; }
  html, body { width: 1200px; height: 900px; overflow: hidden; }
  body {
    position: relative;
    background: var(--stage);
    font-family: "Open Sans", Arial, sans-serif;
  }
  .script { font-family: "Parisienne", cursive; font-weight: 400; white-space: nowrap; }

  /* shared pieces */
  .brand-square {
    position: absolute;
    background: var(--green);
  }
  .photo-frame {
    position: absolute;
    background: var(--white);
    padding: 7px;
    box-shadow: 0 1px 3px rgba(0,0,0,.15);
  }
  .photo {
    width: 100%; height: 100%;
    background: linear-gradient(160deg, var(--photo-b) 0%, var(--photo-a) 70%);
  }
  .ribbon { position: absolute; display: block; }

  /* channel banner */
  .channel-banner {
    position: absolute; left: 266px; top: 130px;
    width: 854px; height: 155px;
    background: var(--white);
    box-shadow: 0 2px 6px rgba(0,0,0,.2);
    overflow: hidden;
  }
  .channel-banner .band {
    position: absolute; left: 0; top: 45px; width: 100%; height: 110px;
    background: var(--green);
  }
  .channel-banner .avatar {
    position: absolute; left: 14px; top: 0; width: 89px; height: 88px;
    background: var(--white); border: 1px solid #c9a9a0;
  }
  .channel-banner .avatar .brand-square { left: 22px; top: 21px; width: 44px; height: 44px; }
  .channel-banner .title {
    position: absolute; left: 250px; top: 72px; width: 350px;
    text-align: center; color: var(--white); font-size: 30px; line-height: 1;
  }
  .channel-banner .tagline {
    position: absolute; left: 250px; top: 111px; width: 350px;
    text-align: center; color: var(--white); font-size: 12.5px;
  }

  /* logo card */
  .logo-card {
    position: absolute; left: 53px; top: 585px;
    width: 419px; height: 163px;
    background: var(--white);
    box-shadow: 0 2px 8px rgba(0,0,0,.2);
  }
  .logo-card .brand-square { left: 70px; top: 42px; width: 80px; height: 80px; }
  .logo-card .wordmark {
    position: absolute; left: 186px; top: 30px;
    color: var(--green); font-size: 34px; line-height: 34px;
  }
  .logo-card .tagline {
    position: absolute; left: 188px; top: 107px;
    color: var(--grey-text); font-size: 15.5px; white-space: nowrap;
  }

  /* circles cover */
  .circles-cover {
    position: absolute; left: 545px; top: 480px;
    width: 586px; height: 348px;
    background: var(--white);
    box-shadow: 0 2px 8px rgba(0,0,0,.25);
    overflow: hidden;
  }
  .circles-cover .band {
    position: absolute; left: 0; top: 80px; width: 100%; height: 268px;
    background: var(--green);
  }
  .circles-cover .brand-square { left: 264px; top: 18px; width: 58px; height: 58px; }
  .circles-cover .title {
    position: absolute; left: 0; top: 100px; width: 100%;
    text-align: center; color: var(--white); font-size: 36px; line-height: 1;
  }
  .circles-cover .tagline {
    position: absolute; left: 0; top: 145px; width: 100%;
    text-align: center; color: var(--white); font-size: 15px;
  }
</style>
</head>
<body>

  <section class="channel-banner" aria-label="Vidstreamo channel cover">
    <svg class="ribbon" style="left:0;top:15px" width="366" height="16" viewBox="0 0 366 16">
      <polygon points="0,0 366,0 356,8 366,16 0,16" fill="var(--pink)"/>
    </svg>
    <svg class="ribbon" style="left:490px;top:15px" width="364" height="16" viewBox="0 0 364 16">
      <polygon points="0,0 364,0 364,16 0,16 10,8" fill="var(--gold)"/>
    </svg>
    <div class="band"></div>
    <div class="avatar"><div class="brand-square" aria-hidden="true"></div></div>
    <div class="brand-square" aria-hidden="true" style="left:407px;top:8px;width:36px;height:36px"></div>
    <div class="photo-frame" style="left:167px;top:58px;width:96px;height:76px">
      <div class="photo" role="img" aria-label="Photo: a child looking through a magnifying glass in the grass"></div>
    </div>
    <div class="photo-frame" style="left:591px;top:58px;width:90px;height:76px">
      <div class="photo" role="img" aria-label="Photo: a mother with two young boys reading on the lawn"></div>
    </div>
    <h2 class="title script">Kitchen Table Scholars</h2>
    <p class="tagline">Making homeschool easier</p>
  </section>

  <section class="logo-card" aria-label="Website logo">
    <div class="brand-square" aria-hidden="true"></div>
    <h1 class="wordmark script">Kitchen Table<br>Scholars</h1>
    <p class="tagline">Making homeschool easier</p>
  </section>

  <section class="circles-cover" aria-label="Orbitly Circles cover">
    <div class="band"></div>
    <svg class="ribbon" style="left:0;top:26px" width="212" height="26" viewBox="0 0 212 26">
      <polygon points="0,0 212,0 196,13 212,26 0,26" fill="var(--pink)"/>
    </svg>
    <svg class="ribbon" style="left:382px;top:26px" width="204" height="26" viewBox="0 0 204 26">
      <polygon points="0,0 204,0 204,26 0,26 16,13" fill="var(--gold)"/>
    </svg>
    <div class="brand-square" aria-hidden="true"></div>
    <h2 class="title script">Kitchen Table Scholars</h2>
    <p class="tagline">Making homeschool easier</p>
    <div class="photo-frame" style="left:11px;top:187px;width:185px;height:146px">
      <div class="photo" role="img" aria-label="Photo: a family lying together on the grass"></div>
    </div>
    <div class="photo-frame" style="left:205px;top:187px;width:184px;height:146px">
      <div class="photo" role="img" aria-label="Photo: a child looking through a magnifying glass in the grass"></div>
    </div>
    <div class="photo-frame" style="left:398px;top:187px;width:176px;height:146px">
      <div class="photo" role="img" aria-label="Photo: a mother with two young boys reading on the lawn"></div>
    </div>
  </section>

</body>
</html>
```